Funky Modern Flyer A5 or Postcard size

Hi, I am looking at a one small flyer (A5 or postcard size) that I can put both on my website on the front page (ie so png) and also send out if necessary.

It has to be modern, funky and hip. My brand is professional / Corporate so it also has to fit in with that brand.

There are 6 attachments:
Example 1 - Kavorra - I like this look, clean, modern, funky and says it all.
Example 2 - Kavora - again another look I like, simple, explanatory
Example 4 - Artisan Bazaar - font is cool on this one but background not so much too much going on but I like the font
Example 5 - Example 4 - Artisan Bazaar - font is cool on this one but background not so much too much going on but I like the font
5 is my logo
Example 6 is something I found on the web this morning which is effective.

It is for a Mentoring and Training program I run called: SKYWARD

What is to be included is the following:
The name: Skyward
Somewhere: Training, Mentoring
My Logo (see attached two options) you can choose which colour suits and I have the source file should you need it
My website and email: www.deliamarsk.example / delia@deliamarsk.example

This wording: This is one of our highest in-demand programs and is based on a background and proven track record by Delia in accelerating sales organisations and their people into stand out high performers. **(NOTE this wording in this paragraph may change and I am open to you changing if you think you can make it more effective!)

Colours: white, black and gold (those are our website colours).

I'd like the Skyward to really stand out.... I have included two fonts that I really like that I got off Artisan Bazaar. However, feel free to suggest other fonts that you think cool or funky!
Updates

Hi everyone, just to add a note to the brief, I am not overly keen on pictures that are really busy. I only like a picture that is minimal and effective. The examples from Artisan Bazaar was more for the Font Style not so much the pictures in the background. The pictures can take away from a design unless done really minimally.....hope this makes sense. Delia Added Wednesday, March 15, 2017

Target Market(s)

My target Market is Corporates but I want a Funky Modern look as a lot of people in Corporates are Millennials as well which is part of my target market

Industry/Entity Type

Information Technology

Requirements
Must have
• What is to be included is the following:
• The name: Skyward
• Somewhere: Training, Mentoring
• My Logo (see attached two options) you can choose which colour suits and I have the source file should you need it
• My website and email: www.deliamarsk.example / delia@deliamarsk.example
• This wording: This is one of our highest in-demand programs and is based on a background and proven track record in high performance and accelerating sales organisations and their people into stand out high performers. (**NOTE this wording may change when final design is picked to be changed as still working in it***)
• Colours: white, black and gold (those are our website colours).
• I'd like the Skyward to really stand out.... I have included two fonts that I really like that I got off Artisan Bazaar. However, feel free to suggest other fonts that you think cool or funky! NOTE: The pictures I have attached is mainly for the FONTS not for the background pictures. I am not that keen on background pictures as it can take away from the font - unless it is minimal
Should not have
• Too many different colours, I like slick, modern, clean. White, gold and black preferred as this is our website colour.
• NOTE: The pictures from Artisan Bazaar I have attached are mainly for the FONTS not for the background pictures. I am not hugely keen on background pictures as it can take away from the font/message - unless the pictures are minimal but effective.

```html
<!DOCTYPE html>
<html lang="en">
<head>
<meta charset="utf-8">
<title>Delia Marsk – Skyward Flyer</title>
<link rel="stylesheet" href="https://fonts.googleapis.com/css2?family=Figtree:wght@400;500&family=Montserrat:wght@300&family=Permanent+Marker&display=swap">
<style>
  :root {
    --page-bg: #ffffff;
    --card-bg: #e6e6e7;
    --gold: #d8b24b;
    --ink: #3d3d40;
    --photo-light: #d2d2d4;
    --photo-dark: #6e6e72;
  }
  * { margin: 0; padding: 0; box-sizing: border-box; }
  html, body {
    width: 1200px;
    height: 1200px;
    overflow: hidden;
    background: var(--page-bg);
  }
  .flyer {
    position: absolute;
    left: 82px;
    top: 234px;
    width: 1046px;
    height: 736px;
    background: var(--card-bg);
    overflow: hidden;
  }
  .brand {
    position: absolute;
    left: 67px;
    top: 66px;
    display: flex;
    align-items: center;
    gap: 22px;
  }
  .brand-square {
    width: 34px;
    height: 34px;
    background: var(--ink);
  }
  .brand-name {
    font-family: "Montserrat", sans-serif;
    font-weight: 300;
    font-size: 48px;
    letter-spacing: 1px;
    color: var(--ink);
    line-height: 1;
  }
  .dancer-photo {
    position: absolute;
    left: 476px;
    top: 10px;
    width: 514px;
    height: 668px;
    background: radial-gradient(ellipse at 55% 60%, var(--photo-dark) 0%, var(--photo-light) 65%, var(--card-bg) 100%);
    border-radius: 40% 40% 20% 20%;
    opacity: 0.7;
  }
  .program-title {
    position: absolute;
    left: 62px;
    top: 178px;
    font-family: "Permanent Marker", cursive;
    font-size: 168px;
    line-height: 1;
    letter-spacing: 6px;
    color: var(--gold);
  }
  .services {
    position: absolute;
    left: 64px;
    top: 420px;
    font-family: "Figtree", sans-serif;
    font-weight: 400;
    font-size: 49px;
    line-height: 1;
    color: var(--gold);
  }
  .summary {
    position: absolute;
    left: 64px;
    top: 482px;
    width: 560px;
    font-family: "Figtree", sans-serif;
    font-weight: 400;
    font-size: 22.5px;
    line-height: 29.6px;
    color: var(--ink);
  }
  .contact {
    position: absolute;
    left: 64px;
    top: 632px;
    list-style: none;
    font-family: "Figtree", sans-serif;
    font-weight: 400;
    font-size: 16.5px;
    line-height: 25px;
    color: var(--gold);
    text-transform: uppercase;
  }
</style>
</head>
<body>
  <main class="flyer">
    <div class="dancer-photo" role="img" aria-label="Black and white photograph of a dancer balancing on her chest and forearms with one leg extended straight up"></div>

    <header class="brand">
      <span class="brand-square"></span>
      <span class="brand-name">DELIA MARSK</span>
    </header>

    <h1 class="program-title">SKYWARD</h1>

    <h2 class="services">TRAINING, MENTORING</h2>

    <p class="summary">This is one of our highest in-demand programs and is based on a background and proven track record by Delia in accelerating sales organisations and their people into stand out high performers.</p>

    <ul class="contact">
      <li>www.deliamarsk.example</li>
      <li>delia@deliamarsk.example</li>
    </ul>
  </main>
</body>
</html>
```